Company brochure for our unique consulting business

We are a small consulting business offering a unique set of services to our clients.. In simple terms we are a business improvement consultancy helping our clients get the best out of their businesses. We work with clients across multiple sectors and deliver a variety of services. We want to put together a brochure to cover these main themes:1. Who we are2. What we do3. The type of people we employ4. The sectors we work inWhile the brochure needs to have a certain corporate feel to it, we don't want it to be "boring" or "stiff". We would like it to have a slightly "friendly" or "informal" feel to it, to reflect the type of organisation we are.We have a company website http://tollandvergeadvisory.com , however we do not want to directly replicate the content or feel as we recognise it needs updating.We would like the brochure to be A4 portrait format. We anticipate requiring 12 sides (including covers) but we are happy to be guided on this based on the content we have provided.The attached ppt file gives the detail of the content to be included and also shows the proposed pagination. For the front cover we would like to try 2 versions, one with the TVA logo and one with the Tolland Verge Advisory logo (a file of both is attached)One of the most important pages will be the "Our Services" page. We would like this to cover the centre fold. In the ppt file we have shown an example layout, but this is where we need most help - we are clearly not graphic designers! This page will be the most used page in sales meetings etc.Also attached is the following:1. file for our TollandVerge Advisory company logo.2. File for our TVA company logo3. Files for Derek's signatures (for under photos) - Owen's to follow4. Photo of Derek & Owen (person in purple shirt to be cropped out)Thank you and really excited to see what everyone comes back with.Derek & Owen

Target Market(s)

Very broad - Manufacturing, Healthcare, Hospitality

Industry/Entity Type

Management Consulting

Font styles to use
Other font styles liked:
• We use Swiss721, but happy to be guided by designer

Colors
3276b5
85abd2
0355a3
333333
5c5c5c
9d9d9d
d9d9d9

Requirements
Must have
• Corporate feel
Nice to have
• Slightly friendly feel
• Our standard "blue" is (CORRECTION) - R55 G96 B146 #376092 and our standard grey is R197 G178, B179 - #B3B2B2, which we would like to keep, but other colours we are happy to be guided on. Brand guidelines attached.

```html
<!DOCTYPE html>
<html lang="en">
<head>
<meta charset="utf-8">
<title>Tolland Verge Advisory – Brochure Covers</title>
<link href="https://fonts.googleapis.com/css2?family=Montserrat:wght@300;400;700;800&family=Open+Sans:wght@300;400;600;700&display=swap" rel="stylesheet">
<style>
  :root {
    --brand-blue: #2a63b3;
    --brand-blue-dark: #1f4f95;
    --logo-blue: #376092;
    --white: #ffffff;
    --page-bg: #e4e4e4;
    --photo-light: #d8d6d2;
    --photo-mid: #a9a5a0;
  }
  * { box-sizing: border-box; margin: 0; padding: 0; }
  html, body { width: 1200px; height: 824px; overflow: hidden; }
  body { background: var(--page-bg); font-family: "Open Sans", Arial, sans-serif; }

  .spread { position: absolute; left: 62px; top: 32px; width: 1076px; height: 760px; overflow: hidden; }
  .page { position: absolute; top: 0; width: 538px; height: 760px; overflow: hidden; }
  .back-cover { left: 0; background: var(--brand-blue); }
  .front-cover { left: 538px; }

  .portrait-fade {
    position: absolute; left: 30px; top: 170px; width: 280px; height: 540px;
    background: radial-gradient(ellipse at 45% 30%, rgba(255,255,255,0.10), rgba(255,255,255,0) 70%);
  }

  .team-photo {
    position: absolute; left: 330px; top: 150px; width: 746px; height: 420px;
    background: linear-gradient(100deg, var(--photo-mid) 0%, var(--photo-light) 30%, #c9c4be 55%, #8a8682 75%, #d9e0e8 100%);
  }

  .back-tagline {
    position: absolute; left: 56px; top: 78px;
    color: var(--white); font-weight: 300; font-size: 28px; letter-spacing: 0.3px; white-space: nowrap;
  }

  .contact { position: absolute; left: 56px; top: 440px; width: 250px; color: var(--white); }
  .contact-title { font-size: 21px; font-weight: 300; }
  .contact-title strong { font-weight: 700; }
  .contact-rule { width: 16px; height: 2px; background: var(--white); margin: 6px 0 12px; }
  .contact-company { font-size: 12px; font-weight: 700; margin-bottom: 8px; }
  .contact-line { display: flex; gap: 8px; font-size: 10px; line-height: 1.35; margin-bottom: 12px; }
  .contact-line svg { flex: none; margin-top: 2px; }

  .name-mark { font-family: "Montserrat", Arial, sans-serif; font-weight: 700; letter-spacing: -1px; }
  .back-mark { position: absolute; left: 56px; top: 670px; color: var(--white); font-size: 36px; line-height: 1; }
  .back-url { position: absolute; right: 40px; top: 690px; color: var(--white); font-size: 10px; display: flex; gap: 5px; align-items: center; }

  .front-shapes { position: absolute; inset: 0; }
  .front-mark { position: absolute; right: 72px; top: 46px; color: var(--logo-blue); font-size: 68px; line-height: 1; }

  .front-title { position: absolute; left: 60px; top: 600px; color: var(--white); }
  .title-line { font-family: "Montserrat", Arial, sans-serif; font-weight: 800; font-size: 22px; line-height: 1.2; white-space: nowrap; }
  .title-line .light { font-weight: 300; }
  .title-rule { width: 28px; height: 4px; background: var(--white); border-radius: 2px; margin-top: 14px; }
  .front-url { position: absolute; right: 48px; top: 700px; color: var(--white); font-size: 11px; display: flex; gap: 5px; align-items: center; }
  .front-url strong, .back-url strong { font-weight: 700; }
  .edge-tab { position: absolute; right: 0; top: 590px; width: 48px; height: 20px; background: var(--white); border-left: 4px solid var(--brand-blue-dark); }
</style>
</head>
<body>
<main class="spread">
  <section class="page back-cover">
    <div class="portrait-fade" role="img" aria-label="Faint portrait of a consultant in the background"></div>
    <p class="back-tagline">better people, better business</p>
    <div class="contact">
      <h2 class="contact-title">Contact <strong>us</strong></h2>
      <div class="contact-rule"></div>
      <p class="contact-company">TVA Limited</p>
      <div class="contact-line">
        <svg width="8" height="10" viewBox="0 0 8 10" aria-hidden="true"><path d="M4 0C1.8 0 0 1.7 0 3.8 0 6.5 4 10 4 10S8 6.5 8 3.8C8 1.7 6.2 0 4 0Z" fill="#fff"/><circle cx="4" cy="3.8" r="1.4" fill="#2a63b3"/></svg>
        <span>Harbour Chambers,<br>Mill Lane<br>Ashbury, AB4 2QT<br>United Kingdom</span>
      </div>
      <div class="contact-line">
        <svg width="10" height="10" viewBox="0 0 10 10" aria-hidden="true"><path d="M2 0.5 3.8 2.8 2.8 4C3.5 5.5 4.5 6.5 6 7.2L7.2 6.2 9.5 8 8.5 9.5C4.5 9.5 0.5 5.5 0.5 1.5Z" fill="none" stroke="#fff" stroke-width="0.9"/></svg>
        <span>+44 (0) 1632 960123</span>
      </div>
      <div class="contact-line">
        <svg width="10" height="8" viewBox="0 0 10 8" aria-hidden="true"><rect x="0.5" y="0.5" width="9" height="7" fill="none" stroke="#fff" stroke-width="0.9"/><path d="M0.5 0.5 5 4.5 9.5 0.5" fill="none" stroke="#fff" stroke-width="0.9"/></svg>
        <span>enquiries@tollandvergegroup.com</span>
      </div>
    </div>
    <div class="back-mark name-mark">tva</div>
    <div class="back-url">
      <svg width="9" height="9" viewBox="0 0 12 12" aria-hidden="true"><circle cx="6" cy="6" r="5" fill="none" stroke="#fff" stroke-width="1.2"/><path d="M1 6H11" stroke="#fff"/></svg>
      <span>www.<strong>tollandverge</strong>group.com</span>
    </div>
  </section>

  <div class="team-photo" role="img" aria-label="Photograph of a team gathered around laptops at a meeting table"></div>

  <section class="page front-cover">
    <svg class="front-shapes" viewBox="0 0 538 760" width="538" height="760" aria-hidden="true">
      <path d="M0 0 H538 V140 Q300 162 0 140 Z" fill="#ffffff"/>
      <path d="M0 560 Q260 490 538 480 V760 H0 Z" fill="#2a63b3"/>
    </svg>
    <div class="front-mark name-mark">tva</div>
    <div class="front-title">
      <div class="title-line">business improvement by</div>
      <div class="title-line">tolland verge <span class="light">advisory</span></div>
      <div class="title-rule"></div>
    </div>
    <div class="edge-tab"></div>
    <div class="front-url">
      <svg width="11" height="11" viewBox="0 0 12 12" aria-hidden="true"><circle cx="6" cy="6" r="5" fill="none" stroke="#fff" stroke-width="1.2"/><path d="M1 6H11M6 1C3.5 3.5 3.5 8.5 6 11M6 1C8.5 3.5 8.5 8.5 6 11" fill="none" stroke="#fff" stroke-width="1"/></svg>
      <span>www.<strong>tollandverge</strong>advisory.com</span>
    </div>
  </section>
</main>
</body>
</html>
```